Lionel Arbusto and Dwight Halvorsen Advertisement

We would like an ad that conveys understated elegance. We are a company that purchases estate jewelry watches and diamonds. We care to a wealthy, upscale clientele.

Target Market(s)

Wealthy upscale.

Industry/Entity Type

It Company

Requirements
Must have
• Elegant Design. Crisp Clean. Attached a doc of how the ad should be arranged.

```html
<!DOCTYPE html>
<html lang="en">
<head>
<meta charset="utf-8">
<title>Lionel Arbusto &amp; Dwight Halvorsen — Ready To Sell?</title>
<link rel="stylesheet" href="https://fonts.googleapis.com/css2?family=Cinzel:wght@400;500&family=Crimson+Text:wght@400&display=swap">
<style>
  :root {
    --ink: #1f1f1f;
    --ink-soft: #3a3a3a;
    --paper: #fbfbfb;
    --paper-shade: #eeeeee;
    --gold-dark: #b8801f;
    --gold-light: #f3d27a;
    --band-top: #26404d;
    --band-bottom: #14232b;
    --band-text: #f4f4f4;
    --stone-light: #ffffff;
    --stone-mid: #d9dde0;
    --stone-dark: #8f969b;
  }
  * { box-sizing: border-box; margin: 0; padding: 0; }
  html, body { width: 960px; height: 1200px; overflow: hidden; background: var(--paper); }
  .ad {
    position: relative;
    width: 960px;
    height: 1200px;
    overflow: hidden;
    font-family: "Cinzel", serif;
    color: var(--ink);
  }
  .ad__backdrop {
    position: absolute;
    inset: 0 0 268px 0;
    background: radial-gradient(ellipse at 50% 40%, var(--paper) 0%, #f5f5f5 60%, var(--paper-shade) 100%);
  }
  .headline {
    position: absolute;
    top: 74px;
    left: 0;
    width: 100%;
    text-align: center;
    font-size: 82px;
    font-weight: 400;
    letter-spacing: 1px;
    line-height: 1;
  }
  .headline__rule {
    position: absolute;
    top: 160px;
    left: 216px;
    width: 528px;
    height: 6px;
  }
  .headline__flourish {
    position: absolute;
    top: 164px;
    left: 440px;
    width: 80px;
    height: 30px;
    background: linear-gradient(180deg, var(--ink-soft), transparent);
    opacity: 0.25;
    border-radius: 0 0 40px 40px;
  }
  .feature-stone {
    position: absolute;
    top: 276px;
    left: 335px;
    width: 256px;
    height: 256px;
    transform: rotate(-12deg);
    border-radius: 28px;
    background: linear-gradient(135deg, var(--stone-light) 0%, var(--stone-mid) 45%, var(--stone-dark) 70%, var(--stone-light) 100%);
    box-shadow: -18px 26px 30px rgba(0,0,0,0.12);
  }
  .brand {
    position: absolute;
    top: 714px;
    left: 0;
    width: 100%;
    text-align: center;
  }
  .brand__name {
    font-size: 27px;
    font-weight: 400;
    letter-spacing: 1.5px;
    line-height: 1;
  }
  .brand__tagline {
    display: flex;
    align-items: center;
    justify-content: center;
    gap: 10px;
    margin-top: 10px;
    font-size: 13px;
    letter-spacing: 1.5px;
    color: var(--ink-soft);
  }
  .brand__tagline::before,
  .brand__tagline::after {
    content: "";
    width: 138px;
    height: 1px;
    background: linear-gradient(90deg, transparent, var(--ink-soft));
  }
  .brand__tagline::after { background: linear-gradient(90deg, var(--ink-soft), transparent); }
  .promise {
    position: absolute;
    top: 808px;
    left: 0;
    width: 100%;
    text-align: center;
    font-size: 24px;
    letter-spacing: 1.5px;
    line-height: 46px;
    color: var(--ink-soft);
  }
  .gold-rule {
    position: absolute;
    top: 925px;
    left: 0;
    width: 100%;
    height: 7px;
    background: linear-gradient(90deg, var(--gold-dark), var(--gold-light) 55%, var(--gold-dark));
  }
  .contact-band {
    position: absolute;
    top: 932px;
    left: 0;
    width: 100%;
    height: 268px;
    background:
      linear-gradient(168deg, rgba(255,255,255,0.05) 0 40%, transparent 40%),
      linear-gradient(180deg, var(--band-top), var(--band-bottom));
  }
  .contact {
    list-style: none;
    padding-top: 48px;
    text-align: center;
    font-family: "Crimson Text", serif;
    font-size: 21px;
    line-height: 35.7px;
    color: var(--band-text);
  }
</style>
</head>
<body>
  <main class="ad">
    <div class="ad__backdrop" role="img" aria-label="Soft quilted white diamond-tufted background"></div>

    <h1 class="headline">Ready To Sell?</h1>
    <svg class="headline__rule" viewBox="0 0 528 6" aria-hidden="true">
      <circle cx="3" cy="3" r="2.5" fill="#1f1f1f"/>
      <line x1="3" y1="3" x2="525" y2="3" stroke="#1f1f1f" stroke-width="1.5"/>
      <circle cx="525" cy="3" r="2.5" fill="#1f1f1f"/>
    </svg>
    <div class="headline__flourish" role="img" aria-label="Small decorative flourish beneath the headline"></div>

    <div class="feature-stone" role="img" aria-label="Photograph of a loose emerald-cut diamond"></div>

    <section class="brand">
      <p class="brand__name">Lionel Arbusto &amp; Dwight Halvorsen</p>
      <p class="brand__tagline">Your Best Option</p>
    </section>

    <p class="promise">Utmost Discretion<br>By Appointment</p>

    <div class="gold-rule"></div>
    <footer class="contact-band">
      <ul class="contact">
        <li>Casa Lumiera</li>
        <li>118-B Alder Row</li>
        <li>Seaview, FL 33999</li>
        <li>support@arbustohalvorsen.com</li>
        <li>555.014.2290</li>
      </ul>
    </footer>
  </main>
</body>
</html>
```